Etiketten für Gin
Zielgruppe
Wir vertreiben einen regionalen Gin mit Fichtennadeln.
Zielgruppe sind Gin-Trinker, Wanderer, Besucher und Bewohner der Bergischen Landes.
Aufgabenstellung
Benötigt wird ein zweiteiliges Etikett für eine 500 ml Flasche (Höhe 320 mm, Durchmesser ca. 75 mm). Datenblatt in der Anlage. Die Flasche wird einen schwarzen Stopfen bekommen,
Das vordere Etikett soll eine Größe von 80 mm (Breite) x 160 mm (Höhe) haben. Das Etikett für die Rückseite soll eine Größe von 60 mm (Breite) x 100 mm (Höhe) haben.
Aufgrund des schwarzen Stopfens wird ein Etikett mit/in schwarz favorisiert. Auf der Vorderseite soll unser Logo (bei den Dateien) abgebildet sein.
Pflichtangaben Vorderseite: auf dem vorderen Etikett müssen die Pflichtangaben zur Nettofüllmenge und zum Alkoholgehalt angegeben sein. Sprich, auf der Vorderseite muss 500 ml und 43 % untergebracht sein. Diese Pflichtangaben müssen zwingend eine Höhe von 4 mm haben (gesetzlich vorgeschrieben). Gleiches gilt für die Verkehrsbezeichnung Gin, die im Logo enthalten ist. Das Wort Gin muss ebenfalls eine Größe von mindestens 4 mm haben.
Auf dem rückwärtigen Etikett müssen folgende Pflichtangaben vorhanden sein:
Talwerk Brand
Lukas Dornfeld
Anton-Weller-Straße 27
51467 Bergisch Gladbach
Des Weiteren wären auf der Rückseite zwei Felder wünschenswert, in die man zum einen die Batch No. und zum anderen die Flaschennummer eintragen kann (Beispiel Bild 'Batch_Flasche'). Zudem ein weißes Feld, in dem später der EAN Code Ei gepflegt werden kann.
Als Text für die Rückseite:
Wo Natur auf Geschmack trifft
Das 'Bergische Gefühl' erleben Sie mit dem Talwerk Brand Gin. Lassen Sie einen naturverbundenen Tag zum Ausklang, beispielsweise nach einer Wanderung, noch einmal an Ihnen vorbeiziehen.
Erinnern Sie sich durch die bei der Herstellung geschmacksgebenden Botanicals von der Fichte an einen erholsamen Spaziergang durch die Wälder des Bergischen Landes.
Mehr Informationen unter
www.talwerk-brand.de
Druckdatenanlieferung laut Druckerei:
Dateiform..

```html
<!DOCTYPE html>
<html lang="de">
<head>
<meta charset="utf-8">
<title>Talwerk Brand Gin – Etiketten</title>
<link href="https://fonts.googleapis.com/css2?family=Big+Shoulders+Display:wght@300;400&family=Roboto+Condensed:wght@400;700&display=swap" rel="stylesheet">
<style>
:root{
  --canvas:#eeeeec;
  --forest-dark:#1c2417;
  --forest-mid:#3d4a36;
  --forest-mist:#8a958a;
  --ink-white:#f4f4f0;
  --gin-green:#5fa02e;
  --band:#d9d9d6;
  --panel:#c9cac6;
  --panel-ink:#2a2f28;
}
*{margin:0;padding:0;box-sizing:border-box}
html,body{width:1200px;height:923px;overflow:hidden;background:var(--canvas)}
.sheet{position:relative;width:1200px;height:923px}
.label{position:absolute;overflow:hidden;color:var(--ink-white);box-shadow:0 6px 14px rgba(0,0,0,.25)}
.forest{position:absolute;inset:0;
  background:
   radial-gradient(ellipse 70% 35% at 50% 18%,rgba(160,170,160,.75),transparent 70%),
   radial-gradient(ellipse 60% 30% at 30% 55%,rgba(110,125,105,.35),transparent 70%),
   linear-gradient(180deg,var(--forest-mist) 0%,var(--forest-mid) 35%,var(--forest-dark) 100%);}
.band{position:absolute;left:0;right:0;height:14px;background:var(--band)}
.band.top{top:0}.band.bottom{bottom:0}
.frame-lines{position:absolute;inset:0;width:100%;height:100%}
/* Front */
.front{left:113px;top:90px;width:560px;height:635px}
.front .fill{position:absolute;top:32px;left:0;right:0;text-align:center;
  font:300 40px/1 'Big Shoulders Display',sans-serif;letter-spacing:3px}
.front .brand-mark{position:absolute;top:190px;left:50%;width:120px;height:120px;margin-left:-60px;
  border-radius:50%;background:var(--gin-green)}
.front .brand-name{position:absolute;top:365px;left:0;right:0;text-align:center;
  font:300 86px/1 'Big Shoulders Display',sans-serif;letter-spacing:2px}
.front .category{position:absolute;top:465px;left:0;right:0;text-align:center;
  font:400 34px/1 'Big Shoulders Display',sans-serif;letter-spacing:12px;color:var(--gin-green)}
.front .origin{position:absolute;bottom:36px;left:0;right:0;text-align:center;
  font:400 26px/1 'Big Shoulders Display',sans-serif;letter-spacing:6px}
/* Back */
.back{left:703px;top:149px;width:384px;height:514px}
.back .headline{position:absolute;top:44px;left:20px;right:20px;text-align:center;
  font:400 46px/1.05 'Big Shoulders Display',sans-serif;letter-spacing:3px;text-transform:uppercase}
.back .story{position:absolute;top:160px;left:36px;right:36px;text-align:center;
  font:400 13px/1.5 'Roboto Condensed',sans-serif}
.back .story p{margin-bottom:14px}
.back .legal{position:absolute;left:0;right:0;bottom:14px;height:110px;background:var(--panel);
  color:var(--panel-ink);display:flex;padding:14px 28px;gap:24px}
.back .producer{font:700 11.5px/1.35 'Roboto Condensed',sans-serif;flex:1}
.back .fields{width:130px;border-left:1px solid #fff;padding-left:12px;
  font:700 9px/1.2 'Roboto Condensed',sans-serif}
.back .field-box{background:#fff;height:18px;margin:3px 0 10px;text-align:center;
  font:400 11px/18px 'Roboto Condensed',sans-serif}
</style>
</head>
<body>
<main class="sheet">
  <section class="label front">
    <div class="forest" role="img" aria-label="Foggy spruce forest photograph"></div>
    <div class="band top"></div>
    <svg class="frame-lines" viewBox="0 0 560 635" aria-hidden="true">
      <g stroke="#f4f4f0" stroke-width="1.5" fill="none" opacity=".85">
        <line x1="0" y1="92" x2="560" y2="92"/>
        <line x1="0" y1="92" x2="60" y2="14"/><line x1="560" y1="92" x2="500" y2="14"/>
        <line x1="0" y1="92" x2="45" y2="140"/><line x1="560" y1="92" x2="515" y2="140"/>
        <line x1="0" y1="551" x2="560" y2="551"/>
        <line x1="0" y1="551" x2="60" y2="621"/><line x1="560" y1="551" x2="500" y2="621"/>
        <line x1="0" y1="551" x2="45" y2="505"/><line x1="560" y1="551" x2="515" y2="505"/>
      </g>
    </svg>
    <div class="fill">43% VOL | 500 ML</div>
    <div class="brand-mark"></div>
    <h1 class="brand-name">TALWERK BRAND</h1>
    <div class="category">•GIN•</div>
    <div class="origin">DISTILLED IN GERMANY</div>
    <div class="band bottom"></div>
  </section>

  <section class="label back">
    <div class="forest" role="img" aria-label="Foggy spruce forest photograph"></div>
    <div class="band top"></div>
    <svg class="frame-lines" viewBox="0 0 384 514" aria-hidden="true">
      <g stroke="#f4f4f0" stroke-width="1.2" fill="none" opacity=".8">
        <line x1="0" y1="40" x2="30" y2="14"/><line x1="384" y1="40" x2="354" y2="14"/>
        <line x1="0" y1="360" x2="40" y2="390"/><line x1="384" y1="360" x2="344" y2="390"/>
      </g>
    </svg>
    <h2 class="headline">Wo Natur auf<br>Geschmack trifft!</h2>
    <div class="story">
      <p>Das ‚Bergische Gefühl‘ erleben Sie mit dem Talwerk Brand Gin. Lassen Sie einen naturverbundenen Tag zum Ausklang, beispielsweise nach einer Wanderung, noch einmal an Ihnen vorbeiziehen.</p>
      <p>Die geschmacksgebenden Botanicals der Fichte erinnern Sie an einen erholsamen Spaziergang durch die Wälder des Bergischen Landes.</p>
      <p>Mehr Informationen unter<br>www.talwerk-brand.de</p>
    </div>
    <div class="legal">
      <address class="producer" style="font-style:normal">Talwerk Brand<br>Lukas Dornfeld<br>Anton-Weller-Straße 27<br>51467 Bergisch Gladbach</address>
      <div class="fields">
        Batch No.
        <div class="field-box">12.09348</div>
        Flaschennummer:
        <div class="field-box">000832</div>
      </div>
    </div>
    <div class="band bottom"></div>
  </section>
</main>
</body>
</html>
```